Window graphics designed like Venetian blinds with message/ graphic poking out

Hi there.
I need someone to create a window graphic that has a changeable picture that I can replace (and get reprinted) depending on whatever offer I'm currently promoting.
visually, I'm after some Venetian blinds graphics that has a secondary picture in the middle. Not sure how, but if it's possible to have the file so that my printer can also change the bands colours, I'd appreciate it.
I have attached a picture that I took of a similar graphic as well as a picture of the windows it'll be on ( 3* 71cm wide *160 in height)
many thanks
Dorian

```html
<!DOCTYPE html>
<html lang="en">
<head>
<meta charset="utf-8">
<title>Severn Drift – Venetian Blind Window Graphic</title>
<link rel="stylesheet" href="https://fonts.googleapis.com/css2?family=Lato:wght@700;900&display=swap">
<style>
  :root {
    --page: #ffffff;
    --slat: #3d7a9d;
    --slat-light: #55a6bf;
    --slat-dark: #2f6586;
    --cord: #1f4f58;
    --text: #ffffff;
    --accent: #63d4e2;
    --badge: #ffffff;
    --badge-text: #1d5a85;
    --skin: #f1b89a;
  }
  * { box-sizing: border-box; margin: 0; padding: 0; }
  html, body { width: 1200px; height: 1200px; overflow: hidden; background: var(--page); }
  .canvas { position: relative; width: 1200px; height: 1200px; font-family: "Lato", sans-serif; }

  .blind-upper {
    position: absolute; top: 196px; width: 345px; height: 427px;
    background: repeating-linear-gradient(to bottom,
      var(--slat) 0 19px, var(--slat-light) 19px 21px, var(--slat-dark) 21px 23px, var(--slat) 23px 33px);
    box-shadow: 0 2px 3px rgba(0,0,0,.15);
  }
  .pane-left  { left: 40px; }
  .pane-mid   { left: 428px; }
  .pane-right { left: 817px; }

  .blind-lower { position: absolute; top: 653px; width: 345px; height: 325px; }

  .panel-text {
    position: absolute; left: 0; width: 100%; text-align: center;
    color: var(--text); font-weight: 700; font-size: 15px; letter-spacing: 3px;
  }
  .panel-text .accent { color: var(--accent); }
  .follow-title { top: 205px; }
  .follow-handle { top: 237px; display: flex; align-items: center; justify-content: center; gap: 6px; }
  .follow-handle .dot { width: 14px; height: 14px; border-radius: 50%; background: #2c4f8a; }
  .contact-title { top: 172px; }
  .contact-phone { top: 204px; }
  .contact-email { top: 235px; font-size: 14px; }

  .badge {
    position: absolute; left: 52px; top: 86px; width: 248px; height: 248px;
    border-radius: 50%; background: var(--badge);
    box-shadow: 0 4px 8px rgba(0,0,0,.3);
    display: flex; flex-direction: column; align-items: center; justify-content: center;
    color: var(--badge-text); font-weight: 900; font-size: 34px; letter-spacing: 4px; line-height: 1.15;
  }

  .hand {
    position: absolute; left: 555px; top: 706px; width: 95px; height: 38px;
    border-radius: 18px 18px 14px 14px;
    background: linear-gradient(to bottom, #f6c9ae, var(--skin));
  }

  .blind-cords { position: absolute; left: 0; top: 0; pointer-events: none; }
</style>
</head>
<body>
<main class="canvas">

  <section class="blind-upper pane-left">
    <p class="panel-text follow-title">FOLLOW US:</p>
    <p class="panel-text follow-handle"><span class="dot"></span><span class="accent">@severndrift</span></p>
  </section>

  <section class="blind-upper pane-mid">
    <div class="badge"><span>SEVERN</span><span>DRIFT</span></div>
  </section>

  <section class="blind-upper pane-right">
    <p class="panel-text contact-title">CONTACT US:</p>
    <p class="panel-text contact-phone">+44(0) 1632 960418</p>
    <p class="panel-text contact-email">tryus@<span class="accent">severndrift</span>.me</p>
  </section>

  <svg class="blind-lower pane-left" viewBox="0 0 345 325" aria-hidden="true">
    <defs>
      <pattern id="slats" width="345" height="33" patternUnits="userSpaceOnUse" y="0">
        <rect width="345" height="33" fill="#3d7a9d"/>
        <rect y="19" width="345" height="2" fill="#55a6bf"/>
        <rect y="21" width="345" height="2" fill="#2f6586"/>
      </pattern>
    </defs>
    <polygon points="0,0 345,49 345,325 0,325" fill="url(#slats)"/>
    <polygon points="0,0 345,49 345,55 0,10" fill="#3d7a9d"/>
    <line x1="0" y1="30" x2="345" y2="64" stroke="#55a6bf" stroke-width="2"/>
    <line x1="0" y1="32" x2="345" y2="66" stroke="#2f6586" stroke-width="2"/>
  </svg>

  <svg class="blind-lower pane-mid" viewBox="0 0 345 325" aria-hidden="true">
    <polygon points="0,49 172,58 345,49 345,325 0,325" fill="url(#slats)"/>
    <polygon points="0,49 172,58 345,49 345,70 0,70" fill="#3d7a9d"/>
    <line x1="0" y1="72" x2="345" y2="72" stroke="#55a6bf" stroke-width="2"/>
    <line x1="0" y1="74" x2="345" y2="74" stroke="#2f6586" stroke-width="2"/>
  </svg>

  <svg class="blind-lower pane-right" viewBox="0 0 345 325" aria-hidden="true">
    <polygon points="0,49 345,0 345,325 0,325" fill="url(#slats)"/>
    <polygon points="0,49 345,0 345,10 0,55" fill="#3d7a9d"/>
    <line x1="0" y1="64" x2="345" y2="30" stroke="#55a6bf" stroke-width="2"/>
    <line x1="0" y1="66" x2="345" y2="32" stroke="#2f6586" stroke-width="2"/>
  </svg>

  <div class="hand" role="img" aria-label="Illustrated hand gripping the blind slat and pulling it down"></div>

  <svg class="blind-cords" width="1200" height="1200" viewBox="0 0 1200 1200" aria-hidden="true">
    <line x1="66" y1="196" x2="66" y2="812" stroke="var(--cord)" stroke-width="3"/>
    <line x1="83" y1="196" x2="83" y2="755" stroke="var(--cord)" stroke-width="3"/>
    <rect x="61" y="808" width="10" height="22" rx="5" fill="var(--cord)"/>
    <rect x="78" y="751" width="10" height="22" rx="5" fill="var(--cord)"/>
  </svg>

</main>
</body>
</html>
```